Flyer für Coaching
Was für ein gewinnbringendes Miteinander. Ich freue mich sehr über diesen gelungenen Flyer - in Postkartenformat. Die Kommunikation war super. Der Designer ist auf alle meine Anmerkungen eingegangen - hat sehr zeitnah reagiert & Geduld bewiesen. Herzlichen Danke für die angenehme Erfahrung.
Zielgruppe
Bei blu4two begleite ich kreativ und individuell auf dem Weg von der Last zur Leichtigkeit - maßgeschneiderte Unterstüzung im 1:1 Verbund supporte ich Personen auf bewusster und unbewusster Ebene (Hypnose/EMDR) dabei im eigenen Leben -> selbstwirksam - selbstwertschätzend zu sein - eigene Potenziale zu entfalten - neue Perspektiven zu entdecken und sich mit Handlungskompetenzen zu bereichern. Meine Zielgruppe sind Erwachsene auf der Suche nach Unterstützung um ihre Herausforderungen zu meistern und nachhaltige Veränderungen für mehr Wohlbefinden & Lebenszufriedenheit zu schaffen. Menschen die sich aktiv mit ihrer persönlichen Entwicklung auseinandersetzen - auseinandersetzen wollen. Z.B. zur Krisenbewältigung, Selbstfürsorge, Gesunderhaltung, Selbstentfaltung.
Headline:
'Selbstbestimmt selbstwirksam leben'
Aufgabenstellung
Ich möchte ein Postkartenformat als Werbeträger - meine derzeitige Karte ist 10,5 cm breit & 14,9 cm hoch mit abgerundeten Ecken - soll die neue auch haben. Vorder- und Rückseite gestaltet - da es eine Werbeträger ist und sie nicht als Postkarte genutzt wir! Ein Handlungsimpuls schon mit einem stimmigen Bild hervorgelockt -> wäre ein Traum. Eine Botschaft mit Nachhaltigkeit - gerne auch so, dass der Leser sie länger aufbewahrt. Alle wichtigen Informationen in kürzester Zeit auf der Vorderseite vermittelt - ich freue mich. Denn Aufmerksamkeit fesselnd + von wem ist die Postkarte - warum bekomme ich sie - schafft Klarheit auf einen Blick. Ich mag Dinge die im Fluss sind - Ecken & scharfe Kanten sind nicht meins. Für den persönlichen Eindruck finde ich ein Bild von mir für den Leser wichtig. Wiedererkennungswert - gerne harmonierend mit meinem Logo welches die Farben #afbd32, #505e68 & #b71673 enthält. Wenn weiß genutzt wird alt-weiß (warmes weiß)bevorzugt.
Sowie den QR-Code auf der Karte einbinden. Ich lege besonderen Wert auf Empathie.
Plaudern & Begegnen - ca. 30 Min. zum Kennenlernen & Fragen klären -> für 0 Euro Einsatz . Dieser Text soll mit drauf - allerdings nicht in den Vordergrund - da es ja eher um den Mehrwert geht
'Wann' eine Person bei mir richtig ist -
'Warum' gerade ich bzw. ein Miteinander ein 'Gewinn' ist. -> Vielleicht hast du Ideen dazu.

```html
<!DOCTYPE html>
<html lang="de">
<head>
<meta charset="utf-8">
<title>blu4two – Flyer Vorder- und Rückseite</title>
<link rel="stylesheet" href="https://fonts.googleapis.com/css2?family=Open+Sans:wght@400;600&family=Playfair+Display:ital,wght@0,700;0,900;1,400;1,700&display=swap">
<style>
  :root {
    --stage: #9ea4b1;
    --magenta: #b71673;
    --sage: #4e6a5c;
    --body: #5a6a62;
    --warm-white: #fdfcf8;
    --mist-light: #eef0ea;
    --mist-mid: #b9c7bb;
    --forest: #5f7d6a;
    --serif: "Playfair Display", Georgia, serif;
    --sans: "Open Sans", Arial, sans-serif;
  }
  * { box-sizing: border-box; margin: 0; padding: 0; }
  html, body { width: 1021px; height: 1200px; overflow: hidden; }
  body { background: var(--stage); position: relative; font-family: var(--sans); }

  .card { position: absolute; background: var(--warm-white); overflow: hidden; }
  .card--front { left: 94px; top: 104px; width: 667px; height: 471px; }
  .card--back { left: 266px; top: 636px; width: 661px; height: 467px; }

  .forest {
    position: absolute; left: 0; top: 0; right: 0;
    background:
      radial-gradient(ellipse at 70% 10%, rgba(250,250,244,.95) 0%, rgba(250,250,244,0) 60%),
      linear-gradient(180deg, var(--mist-light) 0%, var(--mist-mid) 45%, var(--forest) 100%);
  }
  .card--front .forest { height: 394px; }
  .card--back .forest {
    height: 390px;
    background:
      linear-gradient(90deg, rgba(248,248,244,.2) 0%, rgba(248,248,244,.9) 75%),
      linear-gradient(180deg, #f1f2ee 0%, #d3dbd4 55%, #c2cdc4 100%);
  }

  .butterfly { position: absolute; border-radius: 50%; background: rgba(226,150,190,.55); }

  .brand {
    position: absolute; right: 32px; top: 36px;
    display: flex; align-items: center; gap: 8px;
    font-family: var(--sans); font-weight: 600; font-size: 30px; color: var(--magenta);
  }
  .brand-dot { width: 14px; height: 14px; border-radius: 50%; background: var(--magenta); }

  .front-tagline {
    position: absolute; right: 44px; top: 109px;
    font-weight: 600; font-size: 14px; color: var(--sage);
  }
  .headline-pill {
    position: absolute; left: 186px; top: 145px; right: 0; height: 111px;
    background: rgba(250,250,246,.42); border-radius: 56px 0 0 56px;
  }
  .headline {
    position: absolute; right: 33px; top: 160px; text-align: right;
    font-family: var(--serif); font-weight: 700; color: var(--magenta);
    font-size: 41px; line-height: 40px;
  }
  .headline em { font-style: italic; font-weight: 400; }
  .headline .amp { font-style: italic; font-weight: 400; font-size: 30px; }

  .front-band {
    position: absolute; left: 191px; right: 0; top: 314px; height: 58px;
    background: var(--magenta); border-radius: 29px 0 0 29px;
  }
  .front-band p {
    position: absolute; right: 203px; top: 10px; text-align: right;
    color: #fff; font-size: 14px; line-height: 18px; letter-spacing: .04em;
  }
  .portrait {
    position: absolute; left: 469px; top: 229px; width: 174px; height: 165px;
    border-radius: 80px 80px 0 0;
    background: linear-gradient(180deg, #3a3a3a 0%, #6b6b6b 55%, #4a4a4a 100%);
  }

  .contact {
    position: absolute; font-weight: 600; font-size: 13px; color: var(--sage);
    line-height: 19px; letter-spacing: .01em;
  }
  .card--front .contact { left: 0; right: 0; top: 409px; text-align: center; }
  .card--back .contact { left: 32px; top: 405px; }
  .contact .row { display: flex; align-items: center; gap: 6px; white-space: nowrap; }
  .card--front .contact .row { justify-content: center; }
  .card--front .contact .row:first-child { padding-left: 125px; }
  .contact .name { text-transform: uppercase; letter-spacing: .03em; }
  .contact .sep { margin: 0 4px; }
  .contact svg { width: 14px; height: 14px; flex: none; }

  .back-headline {
    position: absolute; left: 23px; top: 24px;
    font-family: var(--serif); font-weight: 900; color: var(--magenta);
    font-size: 35px; line-height: 40px; letter-spacing: -.01em;
  }
  .fit-list {
    position: absolute; list-style: none;
    font-size: 13.5px; line-height: 22px; color: var(--body);
  }
  .fit-list li { position: relative; margin-bottom: 4px; }
  .fit-list li::before {
    content: ""; position: absolute; left: -16px; top: 8px;
    width: 6px; height: 6px; border-radius: 50%; background: var(--magenta);
  }
  .fit-list--one { left: 274px; top: 30px; width: 180px; }
  .fit-list--two { left: 472px; top: 30px; width: 180px; }

  .back-band {
    position: absolute; left: 0; top: 312px; width: 332px; height: 49px;
    background: var(--magenta); border-radius: 0 25px 25px 0;
  }
  .back-band p {
    position: absolute; left: 24px; top: 11px;
    font-family: var(--serif); font-style: italic; color: #fff; font-size: 17px;
  }
</style>
</head>
<body>

<section class="card card--front" aria-label="Vorderseite">
  <div class="forest" role="img" aria-label="Nebliger Nadelwald im Morgenlicht"></div>
  <div class="butterfly" style="left:180px;top:146px;width:40px;height:32px" role="img" aria-label="Aquarell-Schmetterling"></div>
  <div class="butterfly" style="left:102px;top:236px;width:58px;height:46px" role="img" aria-label="Aquarell-Schmetterling"></div>
  <div class="butterfly" style="left:301px;top:298px;width:26px;height:20px" role="img" aria-label="Aquarell-Schmetterling"></div>

  <div class="brand"><span class="brand-dot"></span>blu4two</div>
  <p class="front-tagline">Für alle, die sich Veränderung mit Herz wünschen.</p>

  <div class="headline-pill"></div>
  <h1 class="headline">Selbstbestimmt <span class="amp">&amp;</span><br><em>selbstwirksam</em> leben</h1>

  <div class="front-band"><p>Ich begleite empathisch,<br>mit Struktur und Leichtigkeit.</p></div>
  <div class="portrait" role="img" aria-label="Porträtfoto der Coachin"></div>

  <div class="contact">
    <div class="row">
      <span class="name">Carla Wendtland</span><span class="sep">|</span>
      <svg viewBox="0 0 24 24"><path fill="currentColor" d="M6.6 10.8a15 15 0 0 0 6.6 6.6l2.2-2.2c.3-.3.7-.4 1-.2 1.1.4 2.3.6 3.6.6.6 0 1 .4 1 1V20c0 .6-.4 1-1 1A17 17 0 0 1 3 4c0-.6.4-1 1-1h3.5c.6 0 1 .4 1 1 0 1.3.2 2.5.6 3.6.1.3 0 .7-.2 1z"/></svg>
      <span>0151 . 23 45 6789</span><span class="sep">|</span>
      <svg viewBox="0 0 24 24"><circle cx="12" cy="12" r="4" fill="none" stroke="currentColor" stroke-width="2.4"/><path d="M16 8v5.5a2.5 2.5 0 0 0 5 0V12a9 9 0 1 0-3.5 7.1" fill="none" stroke="currentColor" stroke-width="2.4"/></svg>
      <span>carla@blu4two.de</span>
    </div>
    <div class="row">
      <svg viewBox="0 0 24 24"><path fill="currentColor" d="M12 2a7 7 0 0 0-7 7c0 5 7 13 7 13s7-8 7-13a7 7 0 0 0-7-7zm0 9.5A2.5 2.5 0 1 1 12 6.5a2.5 2.5 0 0 1 0 5z"/></svg>
      <span>Birkenweg 12, 45133 Essen-Werden</span><span class="sep">|</span>
      <svg viewBox="0 0 24 24" fill="none" stroke="currentColor" stroke-width="1.6"><circle cx="12" cy="12" r="9"/><ellipse cx="12" cy="12" rx="4" ry="9"/><path d="M3 12h18M4.5 7.5h15M4.5 16.5h15"/></svg>
      <span>www.blu4two.de</span>
    </div>
  </div>
</section>

<section class="card card--back" aria-label="Rückseite">
  <div class="forest" role="img" aria-label="Heller, nebliger Wald"></div>
  <div class="butterfly" style="left:617px;top:12px;width:44px;height:36px" role="img" aria-label="Aquarell-Schmetterling"></div>
  <div class="butterfly" style="left:24px;top:180px;width:64px;height:52px" role="img" aria-label="Aquarell-Schmetterling"></div>
  <div class="butterfly" style="left:162px;top:266px;width:22px;height:26px" role="img" aria-label="Aquarell-Schmetterling"></div>
  <div class="butterfly" style="left:370px;top:318px;width:40px;height:32px" role="img" aria-label="Aquarell-Schmetterling"></div>

  <h2 class="back-headline">Du bist genau<br>richtig bei<br>mir, wenn …</h2>

  <ul class="fit-list fit-list--one">
    <li>… du das Gefühl hast, irgendwie in deinem Leben festzustecken &amp; nach neuen Perspektiven suchst</li>
    <li>… du das Bedürfnis hast mehr Ruhe &amp; Gelassen&shy;heit in dir zu entwickeln</li>
    <li>… du herausfinden magst, wie du Grenzen setzt &amp; trotzdem verbunden bleibst.</li>
  </ul>
  <ul class="fit-list fit-list--two">
    <li>… du bereit bist, für mehr Lebensqualität und Wohl&shy;gefühl aktiv Veränderun&shy;gen herbeizuführen.</li>
    <li>… du dir mehr Selbst&shy;verständnis wünscht, z.B. Stärken erkennen &amp; nutzen - um Träume zu verwirklichen</li>
    <li>… du wert auf eine ver&shy;trauensvolle und empa&shy;thische Verbindung legst, die dich dabei unterstützt eigene Lösungen für Herausforderungen zu entdecken.</li>
  </ul>

  <div class="back-band"><p>Ich höre hin – mit Herz &amp; Verstand.</p></div>

  <div class="contact">
    <div class="row">
      <span class="name">Carla Wendtland</span><span class="sep">|</span>
      <svg viewBox="0 0 24 24"><path fill="currentColor" d="M6.6 10.8a15 15 0 0 0 6.6 6.6l2.2-2.2c.3-.3.7-.4 1-.2 1.1.4 2.3.6 3.6.6.6 0 1 .4 1 1V20c0 .6-.4 1-1 1A17 17 0 0 1 3 4c0-.6.4-1 1-1h3.5c.6 0 1 .4 1 1 0 1.3.2 2.5.6 3.6.1.3 0 .7-.2 1z"/></svg>
      <span>0151 . 23 45 6789</span><span class="sep">|</span>
      <svg viewBox="0 0 24 24"><circle cx="12" cy="12" r="4" fill="none" stroke="currentColor" stroke-width="2.4"/><path d="M16 8v5.5a2.5 2.5 0 0 0 5 0V12a9 9 0 1 0-3.5 7.1" fill="none" stroke="currentColor" stroke-width="2.4"/></svg>
      <span>carla@blu4two.de</span>
    </div>
    <div class="row">
      <svg viewBox="0 0 24 24"><path fill="currentColor" d="M12 2a7 7 0 0 0-7 7c0 5 7 13 7 13s7-8 7-13a7 7 0 0 0-7-7zm0 9.5A2.5 2.5 0 1 1 12 6.5a2.5 2.5 0 0 1 0 5z"/></svg>
      <span>Birkenweg 12, 45133 Essen-Werden</span><span class="sep">|</span>
      <svg viewBox="0 0 24 24" fill="none" stroke="currentColor" stroke-width="1.6"><circle cx="12" cy="12" r="9"/><ellipse cx="12" cy="12" rx="4" ry="9"/><path d="M3 12h18M4.5 7.5h15M4.5 16.5h15"/></svg>
      <span>www.blu4two.de</span>
    </div>
  </div>
</section>

</body>
</html>
```